Website for Painting Company

Hi,
We are after a Wordpress website design with CSS/HTML Theme for our painting company based in Brisbane, Australia. Our business name is Bevan Molloy Painting Contractors and we have been trading for 33 years.
We want a website that is modern and fresh with a professional image. Our organisation does Commercial, Residential and Insurance Painting projects. I have listed a couple of similar websites that we like the look and feel of. These are a guide only and we are happy to see you own designs with a similar professional image.
http://www.kelvardpainters.com.au/
http://www.unitedcoatworks.com.au/
We are a member of Guild Decorator Australia and I have supplied the logo named "gda" which I have included in the files I have uploaded.
We want a five page site. These are Home Page, Residential, Commercial, Insurance and Contact Us.
I have also uploaded our logo and some pictures labeled Logo,Residential, Commercial, Insurance and Homepage. These should be used on each page listed above.
Updates
Project Deadline Extended
Reason: We are extending because we need more time to go through the designs and give feedback. There are many fantastic designs. Thank you everyone who has contributed!!!!
All the best
Derek
Industry/Entity Type
Painting
Requirements
Must have
- We want a five page site. These are Home Page, Residential, Commercial, Insurance and Contact Us.

```html
<!DOCTYPE html>
<html lang="en">
<head>
<meta charset="utf-8">
<title>Bevan Molloy Painting Contractors</title>
<link rel="stylesheet" href="https://fonts.googleapis.com/css2?family=Arimo:wght@400;700&display=swap">
<style>
:root{
  --red:#c4161c;
  --red-dark:#8e0b10;
  --pink:#fbd2d5;
  --ink:#444;
  --beige:#e7e6da;
  --black:#0d0d0d;
  --white:#fff;
  --grey:#888;
}
*{margin:0;padding:0;box-sizing:border-box}
html,body{width:823px;height:1200px;overflow:hidden}
body{position:relative;font-family:Arimo,Arial,sans-serif;background:var(--white);color:var(--ink)}
.abs{position:absolute}

.topbar{left:0;top:0;width:823px;height:70px;background:linear-gradient(#2b2b2b,#050505);border-bottom:3px solid var(--red)}
.logo{left:82px;top:0;width:158px;height:117px;background:var(--pink);border-radius:0 0 6px 6px;box-shadow:0 3px 8px rgba(0,0,0,.35);display:flex;align-items:center;justify-content:center;gap:6px;flex-direction:column;z-index:2}
.logo .mark{width:18px;height:18px;background:var(--red)}
.logo .name{color:var(--red);font-weight:700;font-size:15px;text-align:center;line-height:1.2}
.mainnav{left:338px;top:35px;display:flex;font-size:10.5px;color:var(--white)}
.mainnav a{color:var(--white);text-decoration:none;padding:5px 8px;letter-spacing:-.3px;margin-right:4px}
.mainnav a.active{background:linear-gradient(#e33a3f,#a50f14);border-radius:6px}
.search{left:583px;top:93px;width:157px;height:23px;border:2px solid #d2d2d2;border-radius:12px;font-size:9px;color:#999;padding:5px 12px;background:#fafafa}
.search svg{position:absolute;right:10px;top:3px}

.band-beige{left:0;top:318px;width:823px;height:512px;background:var(--beige);border-top:1px solid #d8d6c8;z-index:0}
.hero{left:82px;top:143px;width:658px;height:232px;background:var(--white);border:1px solid #d5d5d5;box-shadow:0 8px 14px rgba(0,0,0,.15);z-index:2}
.hero-bg{left:7px;top:7px;width:644px;height:218px;background:linear-gradient(90deg,#e9585a,#ea6b6a 45%,#d9545a)}
.hero-photo{left:320px;top:26px;width:250px;height:165px;background:linear-gradient(#cfd1d0,#a79a85);transform:rotate(-6deg);border:5px solid #f3eee6;box-shadow:0 3px 8px rgba(0,0,0,.3)}
.hero h1{left:22px;top:36px;color:var(--white);font-size:20px;font-weight:700;line-height:28px;text-shadow:0 1px 2px rgba(0,0,0,.3)}
.hero p{left:24px;top:96px;color:var(--white);font-size:15px}
.btn{background:linear-gradient(#e02a30,#a80e13);color:var(--white);font-weight:700;font-size:14px;border-radius:6px;text-align:center;box-shadow:0 2px 4px rgba(0,0,0,.3)}
.btn-tour{left:43px;top:164px;width:108px;height:29px;line-height:29px}
.btn-portfolio{left:174px;top:163px;width:108px;height:30px;line-height:30px}

.card{left:82px;width:658px;background:var(--white);border:1px solid #d0d0d0;border-radius:3px;box-shadow:0 1px 4px rgba(0,0,0,.12);z-index:2}
.card h2,.section-title{font-size:12.5px;font-weight:400;color:var(--red);display:flex;align-items:center;gap:3px}
.card h2{position:absolute;left:6px;top:12px}
.card .body{position:absolute;left:24px;top:28px;width:534px;font-size:9.1px;line-height:13.5px;color:#555;letter-spacing:-.1px}
.card .more{position:absolute;left:24px;font-size:9px;color:var(--red)}
.icon-slot{position:absolute;border-radius:8px}
.section-title{left:87px;top:725px;font-size:13px;z-index:2}
.bucket{left:664px;top:672px;width:48px;height:68px;background:linear-gradient(#c62226,#2a2a2a);border-radius:4px;z-index:2}

.carousel{left:82px;top:747px;width:658px;height:135px;background:linear-gradient(#fbfbfb,#e9e9e9);border:1px solid #cfcfcf;border-radius:3px;box-shadow:0 2px 6px rgba(0,0,0,.25);z-index:5}
.thumb{position:absolute;top:29px;width:118px;height:71px;border:1px solid #ccc;padding:2px;background:var(--white)}
.thumb div{width:100%;height:100%}
.caption{position:absolute;top:109px;font-size:8px;color:#555}
.chev{position:absolute;top:40px}

.footer{left:0;top:830px;width:823px;height:330px;background:linear-gradient(#1e1e1e,#040404);z-index:1}
.footer h3{position:absolute;top:100px;color:var(--white);font-size:16px;font-weight:700}
.footer h3 span{color:var(--grey)}
.footer .copy{position:absolute;left:88px;top:137px;width:200px;font-size:9.3px;line-height:16px;color:#eee}
.btn-suggest{position:absolute;left:91px;top:273px;width:88px;height:20px;line-height:20px;font-size:9.5px;font-weight:400;border-radius:2px;box-shadow:none}
.blog{position:absolute;left:327px;top:130px;width:163px;list-style:none;font-size:9px;color:#eee}
.blog li{height:28px;line-height:28px;padding-left:3px;border-bottom:1px dotted #777}
.badge{position:absolute;left:527px;top:131px;width:190px;height:175px;background:var(--white)}
.bottombar{left:0;top:1160px;width:823px;height:40px;background:#2b2b2b;border-top:1px solid #555;z-index:1}
.bottombar .c{position:absolute;left:88px;top:17px;font-size:8px;color:#ddd}
.bottombar nav{position:absolute;left:390px;top:14px;display:flex;gap:15px;font-size:10px;color:var(--white)}
</style>
</head>
<body>
<header>
  <div class="abs topbar"></div>
  <div class="abs logo"><span class="mark"></span><span class="name">Bevan Molloy<br>Painting Contractors</span></div>
  <nav class="abs mainnav"><a class="active">HOME</a><a>RESIDENTIAL</a><a>COMMER CIAL</a><a>INSURANCE</a><a>CONTACT US</a></nav>
  <div class="abs search">search....
    <svg width="16" height="14" viewBox="0 0 16 14"><circle cx="6" cy="6" r="4.5" fill="none" stroke="#888" stroke-width="1.6"/><line x1="9.5" y1="9" x2="14" y2="12.5" stroke="#888" stroke-width="2"/></svg>
  </div>
</header>

<div class="abs band-beige"></div>

<footer class="abs footer">
  <h3 style="left:88px">Suggestions for <span>US</span>?</h3>
  <p class="copy">Sed ut perspiciatis unde omnis iste natus error sit voluptatem accusantium doloremque laudantium, totam rem aperiam.<br><br>Eaque ipsa quae ab illo inventore veritatis et quasi architecto beatae vitae dicta sunt explicabo est magna quisit.</p>
  <a class="btn btn-suggest">Make a Suggestion</a>

  <h3 style="left:327px">Latest From the <span>Blog</span></h3>
  <ul class="blog">
    <li>Sed ut perspiciatis unde omnis iste</li>
    <li>Inventore veritatis et unde omnis ut</li>
    <li>Perspiciatis unde omnis iste oplo</li>
    <li>Inventop goplu hiop</li>
    <li>Inventop goplu hiop</li>
  </ul>

  <h3 style="left:527px">Member of <span>GDA</span></h3>
  <div class="badge" role="img" aria-label="Guild Decorator Australia member badge"></div>
</footer>

<section class="abs hero">
  <div class="abs hero-bg" role="img" aria-label="Red painted living room interior"></div>
  <div class="abs hero-photo" role="img" aria-label="Stack of photos showing a bright open-plan dining room"></div>
  <h1 class="abs">Residential Painters Interior<br>or Exterior Combined Painting</h1>
  <p class="abs">The Reliable Painters in Australia</p>
  <a class="abs btn btn-tour">Take The Tour</a>
  <a class="abs btn btn-portfolio">Portfolio</a>
</section>

<svg width="0" height="0" style="position:absolute"><defs><symbol id="tick" viewBox="0 0 16 16"><path d="M1 9l4 5L15 1l-9 9z" fill="#c4161c"/></symbol></defs></svg>

<article class="abs card" style="top:421px;height:111px">
  <h2><svg width="16" height="16"><use href="#tick"/></svg>Welcome To our Site</h2>
  <p class="body">Lorem ipsum dolor sit amet, consectetur adipisicing elit, sed do eiusmod tempor incididunt ut labore et dolore magna aliqua. Ut enim ad minim veniam.Lorem ipsum dolor sit amet, consectetur adipisicing elit, sed do eiusmod tempor incididunt ut labore et dolore magna aliqua. Ut enim ad minim veniam.Lorem ipsum dolor sit amet, consectetur adipisicing elit, sed do eiusmod tempor incididunt ut labore et dolore magna aliqua. Ut enim ad minim veniam.</p>
  <a class="more" style="top:92px">Read more... ▸</a>
  <div class="icon-slot" style="left:568px;top:26px;width:58px;height:58px;background:linear-gradient(#6bb7e6,#2c7fb8)" role="img" aria-label="Address book icon"></div>
</article>

<article class="abs card" style="top:557px;height:111px">
  <h2><svg width="16" height="16"><use href="#tick"/></svg>Testimonial</h2>
  <p class="body">Ut enim ad minim veniam. Lorem ipsum dolor sit amet, consectetur adipisicing elit, sed do eiusmod tempor incididunt ut labore et dolore magna aliqua. Lorem ipsum dolor sit amet, consectetur adipisicing elit, sed do eiusmod tempor incididunt ut labore et dolore magna aliqua. Ut enim ad minim veniam.Lorem ipsum dolor sit amet, consectetur adipisicing elit, sed do eiusmod tempor incididunt ut labore et dolore magna aliqua. Ut enim ad minim veniam.</p>
  <a class="more" style="top:91px">View more... ▸</a>
  <div class="icon-slot" style="left:556px;top:26px;width:72px;height:62px;background:linear-gradient(90deg,#3d7cc9,#e0554f)" role="img" aria-label="Two customers icon"></div>
</article>

<div class="abs bucket" role="img" aria-label="Red paint tin with brush"></div>
<h2 class="abs section-title"><svg width="17" height="17"><use href="#tick"/></svg>Featured House Paint</h2>

<section class="abs carousel">
  <svg class="chev" style="left:16px" width="30" height="52" viewBox="0 0 30 52"><polyline points="28,2 4,26 28,50" fill="none" stroke="#bdbdbd" stroke-width="3"/></svg>
  <svg class="chev" style="left:612px" width="30" height="52" viewBox="0 0 30 52"><polyline points="2,2 26,26 2,50" fill="none" stroke="#bdbdbd" stroke-width="3"/></svg>
  <div class="thumb" style="left:69px"><div role="img" aria-label="Modern white office building" style="background:linear-gradient(#8fb3d9,#dcdcdc 60%,#7a8a70)"></div></div>
  <div class="thumb" style="left:202px"><div role="img" aria-label="White contemporary house" style="background:linear-gradient(#3f78c4,#e8e8e8 60%,#666)"></div></div>
  <div class="thumb" style="left:335px"><div role="img" aria-label="Two-storey family home" style="background:linear-gradient(#6fa4d8,#c9c3b5 55%,#4f6b3a)"></div></div>
  <div class="thumb" style="left:468px"><div role="img" aria-label="Bright painted interior" style="background:linear-gradient(#e8e8e8,#b9a58c)"></div></div>
  <span class="caption" style="left:74px">Lorem Ipsum</span>
  <span class="caption" style="left:206px">Ipsim optopli</span>
  <span class="caption" style="left:339px">Porto Oplopyi</span>
  <span class="caption" style="left:471px">Porto Opolopu</span>
</section>

<div class="abs bottombar">
  <span class="c">Copyright © 2012 All Rights Reserved</span>
  <nav><span>HOME</span><span>RESIDENTIAL</span><span>COMMER CIAL</span><span>INSURANCE</span><span>CONTACT US</span></nav>
</div>
</body>
</html>
```